Wordpress design for lovely french B&B - Mas des Ormeaux

We need a Wordpress design for a B&B located in eastern France.
The current website (designed by the previous owners) is here: http://www.masdesormeaux-exemple.fr. But it's not what we want, it has some photos so you can have a look at what it looks like.
New photos will be taken.

The new design should be fresh, modern and engaging and reflect the fact that it is a lovely B&B with 5 rooms. It is located in a lovely french village, close to the german and swiss border. It is perfectly located, close to the city, stores and highways, and also close to the country side.

The website should be able to describe each of the 5 rooms (1 page per room, with photos, description, price and booking).
The website should also have a pages to display the surrounding activities (one page with country side activities and one page with city activities) and also have a map for directions as well as a contact page with a form.
We will include a wordpress booking plugin so people can book online.

Target Market(s)

People visiting the french country side

Industry/Entity Type

Online

Logo Text

Le Mas des Ormeaux

Font styles to use
Script

Requirements
Must have
• Should feel like it's in the country side, but also feel like it's a little bit of luxury but not too much
Should not have
• I used B&B term to make it understandable, but it should not use the term B&B. It should use the french term "Gîte"

```html
<!DOCTYPE html>
<html lang="en">
<head>
<meta charset="utf-8">
<title>Le Mas des Ormeaux — Gîte</title>
<link rel="stylesheet" href="https://fonts.googleapis.com/css2?family=Cinzel:wght@400;700&family=Open+Sans:ital,wght@0,400;0,600;0,700;1,400;1,700&family=Dancing+Script:wght@500&display=swap">
<style>
:root{
  --accent:#e5535c;
  --accent-dark:#c93f48;
  --title:#d9484f;
  --dark:#262626;
  --page:#f1f0ef;
  --band:#dcdcdc;
  --text:#333;
  --white:#fff;
}
*{margin:0;padding:0;box-sizing:border-box}
html,body{width:1200px;height:2442px;overflow:hidden}
body{position:relative;background:var(--page);font-family:"Open Sans",Arial,sans-serif;color:var(--text)}
.abs{position:absolute}
h1,h2,h3{font-weight:400}
.topbar{left:0;top:0;width:1200px;height:138px;background:linear-gradient(#1c1c1c,#3a3a3a)}
.logo{font-family:"Cinzel",serif;font-weight:400;color:var(--white);font-size:28px;letter-spacing:.5px;white-space:nowrap}
.top-logo{left:52px;top:22px}
.contact-line{top:32px;font-size:12px;font-weight:600;color:var(--white);display:flex;align-items:center;gap:8px;white-space:nowrap}
.contact-line span{color:var(--accent);font-weight:400}
.nav{left:49px;top:94px;width:1096px;height:48px;background:linear-gradient(#fafafa,#dcdcdc);display:flex;border-radius:2px;box-shadow:0 2px 3px rgba(0,0,0,.3)}
.nav a{font-size:13px;color:#333;text-decoration:none;display:flex;align-items:center;justify-content:center;text-transform:uppercase}
.nav a.active{background:var(--accent);color:var(--white)}
.hero{left:0;top:138px;width:1200px;height:497px;background:linear-gradient(160deg,#3b2a24 0%,#6d5a52 30%,#c9c2bb 55%,#8d847d 80%,#4a3e39 100%)}
.hero-arrow{top:338px;width:44px;height:44px;border-radius:50%;border:2px solid rgba(255,255,255,.8);background:rgba(0,0,0,.25)}
.slide-caption{left:101px;top:412px;width:326px;height:60px;background:rgba(40,40,40,.75);font-family:"Dancing Script",cursive;color:var(--white);font-size:30px;padding:8px 0 0 10px;white-space:nowrap}
.booking{left:0;top:527px;width:1200px;height:108px;background:rgba(30,30,30,.9)}
.booking-label{left:120px;top:569px;font-size:17px;font-weight:600;color:var(--white)}
.field{top:563px;height:36px;background:var(--white);font-size:13px;color:#555;padding:9px 8px}
.book-btn{left:965px;top:563px;width:118px;height:36px;background:#111;border:1px solid #444;color:var(--white);font-size:15px;text-align:center;line-height:34px}
.sec-title{font-family:"Cinzel",serif;color:var(--title);white-space:nowrap}
.center{left:0;width:1200px;text-align:center}
.h-center{font-size:34px}
.sub{font-size:16px;font-weight:700;font-style:italic;color:#222}
.intro{left:94px;top:748px;width:1013px;font-size:12px;line-height:22.5px;text-align:center;color:#444}
.country{left:0;top:863px;width:1200px;height:374px;background:var(--band)}
.h-left{font-size:24px}
.avatar{width:110px;height:110px;border-radius:50%;border:4px solid #222;background:linear-gradient(135deg,#6b4a33,#c78a56)}
.item-title{left:182px;font-size:12.5px;font-weight:600;color:#222}
.item-text{left:182px;width:400px;font-size:12px;line-height:22px;color:#444}
.video{left:641px;top:890px;width:507px;height:318px;background:linear-gradient(135deg,#7a3a2a,#c7865f 45%,#e8d8c0 70%,#8a4d33)}
.video-bar{left:641px;top:890px;width:507px;height:26px;background:rgba(0,0,0,.85);color:#ddd;font-size:11px;padding:6px 10px}
.video-controls{left:641px;top:1180px;width:507px;height:28px;background:#1b1b1b;color:#ccc;font-size:10px;padding:8px 60px}
.play{left:858px;top:1025px;width:72px;height:50px;border-radius:10px;background:rgba(20,20,20,.85)}
.thumb{width:215px;height:215px;border:4px solid #ddd}
.offers li{list-style:none;position:absolute;left:73px;font-size:15px;font-style:italic;font-weight:600;color:#222;display:flex;gap:9px;align-items:center;white-space:nowrap}
.portrait{left:512px;top:1934px;width:188px;height:188px;border-radius:50%;border:7px solid #fff;box-shadow:0 0 0 1px #ccc;background:linear-gradient(135deg,#d8c7b5,#8c7565)}
.quote{left:723px;top:1978px;width:425px;font-size:12px;font-style:italic;line-height:25px;color:#333}
.footer{left:0;top:2178px;width:1200px;height:218px;background:#2a2a2a}
.f-head{color:var(--white);font-size:21px;white-space:nowrap}
.f-text{color:var(--white);font-size:12px;font-weight:600;white-space:nowrap}
.input{left:52px;top:2299px;width:252px;height:36px;background:var(--white);font-size:12px;color:#666;padding:10px 8px}
.submit{left:319px;top:2299px;width:125px;height:36px;background:var(--accent);color:var(--white);font-size:16px;text-align:center;line-height:36px;border-radius:2px}
.social{top:2295px;width:36px;height:36px;border-radius:50%;border:2px solid #bbb}
.copy{left:0;top:2396px;width:1200px;height:46px;background:var(--accent);color:var(--white);font-size:12px;padding:14px 168px}
</style>
</head>
<body>

<header>
  <div class="abs topbar"></div>
  <div class="abs logo top-logo">Le Mas des Ormeaux</div>
  <div class="abs contact-line" style="left:672px">
    <svg width="16" height="16" viewBox="0 0 24 24"><path fill="#fff" d="M6.6 10.8a15 15 0 0 0 6.6 6.6l2.2-2.2a1 1 0 0 1 1-.25 11.4 11.4 0 0 0 3.6.57 1 1 0 0 1 1 1V20a1 1 0 0 1-1 1A17 17 0 0 1 3 4a1 1 0 0 1 1-1h3.5a1 1 0 0 1 1 1c0 1.25.2 2.45.57 3.57a1 1 0 0 1-.25 1z"/></svg>
    CALL US : <span>+33 6 12 48 90 27</span>
  </div>
  <div class="abs contact-line" style="left:882px">
    <svg width="15" height="12" viewBox="0 0 24 18"><rect width="24" height="18" rx="2" fill="#fff"/><path d="M1 2l11 8 11-8" stroke="#333" stroke-width="2" fill="none"/></svg>
    EMAIL US : <span>hello@gite-ormeaux.fr</span>
  </div>
  <nav class="abs nav">
    <a class="active" style="width:93px" href="#">Home</a>
    <a style="width:100px" href="#">Photos</a>
    <a style="width:100px" href="#">Price</a>
    <a style="width:130px" href="#">Booking</a>
    <a style="width:205px" href="#">Country Activies</a>
    <a style="width:170px" href="#">City Activies</a>
    <a style="width:110px" href="#">Map</a>
    <a style="width:188px" href="#">Contact</a>
  </nav>
</header>

<section>
  <div class="abs hero" role="img" aria-label="Photo of a modern guest bedroom with a white bed and dark wood furniture"></div>
  <div class="abs hero-arrow" style="left:18px"><svg width="40" height="40" viewBox="0 0 40 40"><path d="M23 13l-7 7 7 7" stroke="#fff" stroke-width="2.5" fill="none"/></svg></div>
  <div class="abs hero-arrow" style="left:1145px"><svg width="40" height="40" viewBox="0 0 40 40"><path d="M17 13l7 7-7 7" stroke="#fff" stroke-width="2.5" fill="none"/></svg></div>
  <div class="abs slide-caption">Luxuriously Accommodate</div>
  <div class="abs booking"></div>
  <div class="abs booking-label">Online Reservations</div>
  <div class="abs field" style="left:306px;width:169px">Check-in</div>
  <div class="abs field" style="left:497px;width:167px">Check-Out</div>
  <div class="abs field" style="left:684px;width:120px">Rooms</div>
  <div class="abs field" style="left:825px;width:119px">Guests</div>
  <svg class="abs" style="left:445px;top:573px" width="16" height="16" viewBox="0 0 16 16"><rect x="1" y="2" width="14" height="13" fill="none" stroke="#888"/><path d="M1 6h14M5 0v4M11 0v4" stroke="#888"/></svg>
  <svg class="abs" style="left:633px;top:573px" width="16" height="16" viewBox="0 0 16 16"><rect x="1" y="2" width="14" height="13" fill="none" stroke="#888"/><path d="M1 6h14M5 0v4M11 0v4" stroke="#888"/></svg>
  <svg class="abs" style="left:783px;top:577px" width="12" height="9"><path d="M0 0h12L6 9z" fill="#333"/></svg>
  <svg class="abs" style="left:924px;top:577px" width="12" height="9"><path d="M0 0h12L6 9z" fill="#333"/></svg>
  <div class="abs book-btn">BOOK NOW</div>
</section>

<section>
  <h1 class="abs sec-title center h-center" style="top:658px">Welcome to Our Gîte</h1>
  <p class="abs sub center" style="top:705px">WE OFFER YOU THE BEST GÎTE WITH AN LUXURY IMPRESSIVE</p>
  <p class="abs intro">This is a plain version of Lorem Ipsum. Proin gravida nibh vel velit auctor aliquet. Aenean sollicitudin, lorem quis bibendum auctor, nisi elit consequat ipsum, nec sagittis sem nibh id elit. Duis sed odio sit amet nibh vulputate cursus a sit amet mauris. Morbi accumsan ipsum velit. Nam nec tellus a odio tincidunt auctor a ornare odio. Sed non mauris vitae erat consequat auctor eu in elit. Class aptent taciti sociosqu ad litora torquent per conubia nostra.</p>
</section>

<section>
  <div class="abs country"></div>
  <h2 class="abs sec-title h-left" style="left:52px;top:876px">Country Activies</h2>
  <div class="abs avatar" style="left:56px;top:936px" role="img" aria-label="Round photo of a guest cycling in the countryside"></div>
  <div class="abs avatar" style="left:56px;top:1070px" role="img" aria-label="Round photo of a guest enjoying a local activity"></div>
  <h3 class="abs item-title" style="top:954px">PROIN GRAVIDA NIBH VEL VELIT AUCTOR ALIQUET</h3>
  <p class="abs item-text" style="top:981px">Aenean sollicitudin, lorem quis bibendum auctor, nisi elit consequat ipsum, nec sagittis sem nibh id elit.</p>
  <h3 class="abs item-title" style="top:1086px">PROIN GRAVIDA NIBH VEL VELIT AUCTOR ALIQUET</h3>
  <p class="abs item-text" style="top:1113px">Aenean sollicitudin, lorem quis bibendum auctor, nisi elit consequat ipsum, nec sagittis sem nibh id elit.</p>
  <div class="abs video" role="img" aria-label="Video still of the gîte living room with sofas and a fireplace"></div>
  <div class="abs video-bar">31288.flv</div>
  <div class="abs play"><svg width="72" height="50"><path d="M29 15l16 10-16 10z" fill="#fff"/></svg></div>
  <div class="abs video-controls">0:00 / 0:26</div>
  <svg class="abs" style="left:652px;top:1187px" width="14" height="14"><path d="M2 1l10 6-10 6z" fill="#ccc"/></svg>
</section>

<section>
  <h2 class="abs sec-title center h-center" style="top:1264px">Photo</h2>
  <p class="abs sub center" style="top:1311px">WE OFFER YOU THE BEST GÎTE WITH AN LUXURY IMPRESSIVE</p>
  <div class="abs thumb" style="left:124px;top:1369px;background:linear-gradient(#9fb0c4,#5f7a3e 55%,#c9d9df)" role="img" aria-label="Photo of the pool terrace with sun loungers"></div>
  <div class="abs thumb" style="left:370px;top:1369px;background:linear-gradient(#e6e2dc,#3a2a24 60%,#cdbfae)" role="img" aria-label="Photo of a lounge with a leather sofa"></div>
  <div class="abs thumb" style="left:615px;top:1369px;background:linear-gradient(#b7c3c9,#7e8b55 50%,#a8455a)" role="img" aria-label="Photo of a flowered garden terrace with a parasol"></div>
  <div class="abs thumb" style="left:863px;top:1369px;background:linear-gradient(#e4d2b4,#8d6a44 60%,#b5876a)" role="img" aria-label="Photo of an attic bedroom"></div>
  <div class="abs thumb" style="left:124px;top:1615px;background:linear-gradient(#8a9a5a,#5b6d33 60%,#a45a4b)" role="img" aria-label="Photo of the garden and countryside"></div>
  <div class="abs thumb" style="left:370px;top:1615px;background:linear-gradient(#7b7b6a,#4f6a2e 55%,#cfcfc5)" role="img" aria-label="Photo of a garden table with white chairs"></div>
  <div class="abs thumb" style="left:615px;top:1615px;background:linear-gradient(#c9b79a,#6b4a38 55%,#a48373)" role="img" aria-label="Photo of a bedroom with bedside lamps"></div>
  <div class="abs thumb" style="left:863px;top:1615px;background:linear-gradient(#6b4a30,#d8cbb8 45%,#7d5168)" role="img" aria-label="Photo of a bedroom with wooden beams"></div>
</section>

<section>
  <h2 class="abs sec-title h-left" style="left:52px;top:1892px">Special Offers</h2>
  <ul class="offers">
    <li style="top:1943px"><svg width="15" height="14"><rect x="0.5" y="2.5" width="11" height="11" fill="none" stroke="#e5535c"/><path d="M3 7l3 3 8-9" stroke="#e5535c" stroke-width="2" fill="none"/></svg>Aenean sollicitudin lorem quis bibendum auctorss</li>
    <li style="top:1977px"><svg width="15" height="14"><rect x="0.5" y="2.5" width="11" height="11" fill="none" stroke="#e5535c"/><path d="M3 7l3 3 8-9" stroke="#e5535c" stroke-width="2" fill="none"/></svg>Sagittis sem nibh id elitis sed odio sit amet nibhed</li>
    <li style="top:2010px"><svg width="15" height="14"><rect x="0.5" y="2.5" width="11" height="11" fill="none" stroke="#e5535c"/><path d="M3 7l3 3 8-9" stroke="#e5535c" stroke-width="2" fill="none"/></svg>Morbi accumsan ipsum veli nec tellus tinciduntth</li>
    <li style="top:2044px"><svg width="15" height="14"><rect x="0.5" y="2.5" width="11" height="11" fill="none" stroke="#e5535c"/><path d="M3 7l3 3 8-9" stroke="#e5535c" stroke-width="2" fill="none"/></svg>Sagittis sem nibh id elitis sed odio sit amet nibhes</li>
    <li style="top:2078px"><svg width="15" height="14"><rect x="0.5" y="2.5" width="11" height="11" fill="none" stroke="#e5535c"/><path d="M3 7l3 3 8-9" stroke="#e5535c" stroke-width="2" fill="none"/></svg>Morbi accumsan ipsum veli nec tellus tinciduntted</li>
  </ul>
  <h2 class="abs sec-title h-left" style="left:510px;top:1892px">What Our Customers Say</h2>
  <div class="abs portrait" role="img" aria-label="Round photo of a smiling couple of guests"></div>
  <div class="abs" style="left:716px;top:1932px;font-family:Georgia,serif;font-size:44px;color:var(--accent);line-height:1">&ldquo;</div>
  <p class="abs quote">Lorem Ipsum Proin gravida nibh vel velit auctor aliquet. Aenean sollicitudin, lorem quis bibendum auctor, nisi elit consequat ipsum, nec sagittis sem nibh id elit. Duis sed odio sit amet nibh vulputate cursus a sit amet mauris. Morbi accumsan ipsum velit.</p>
  <p class="abs" style="left:726px;top:2078px;font-size:15px;font-weight:700;color:#222">- Claire Vernet-</p>
</section>

<footer>
  <div class="abs footer"></div>
  <h3 class="abs f-head" style="left:55px;top:2216px">NewsLetter</h3>
  <p class="abs f-text" style="left:54px;top:2262px;font-size:15px">Join us for interesting News and Offer!</p>
  <div class="abs input">Enter your email</div>
  <div class="abs submit">SUBMIT</div>

  <div class="abs logo" style="left:526px;top:2214px;font-size:25px">Le Mas des Ormeaux</div>
  <h3 class="abs f-head" style="left:542px;top:2251px">Location</h3>
  <p class="abs f-text" style="left:543px;top:2287px">Gîte Company, 18 rue des Tilleuls</p>
  <p class="abs f-text" style="left:543px;top:2316px">bonjour@gite-exemple.org</p>
  <p class="abs f-text" style="left:543px;top:2344px">1(555) 203-4417</p>

  <h3 class="abs f-head" style="left:856px;top:2213px;letter-spacing:1px">Let's Socialize</h3>
  <p class="abs" style="left:858px;top:2258px;font-size:12px;color:#999;letter-spacing:1px">Follow us:</p>
  <div class="abs social" style="left:858px"></div>
  <div class="abs social" style="left:903px"></div>
  <div class="abs social" style="left:949px"></div>
  <div class="abs social" style="left:993px"></div>
  <div class="abs social" style="left:1039px"></div>
  <div class="abs social" style="left:1083px"></div>
  <svg class="abs" style="left:864px;top:2353px" width="20" height="16" viewBox="0 0 20 16"><path d="M1 5a13 13 0 0 1 18 0M4 8.5a8.5 8.5 0 0 1 12 0M7 12a4 4 0 0 1 6 0" stroke="#e5535c" stroke-width="2" fill="none"/><circle cx="10" cy="14.5" r="1.5" fill="#e5535c"/></svg>
  <p class="abs f-text" style="left:899px;top:2354px;font-weight:400">Free WiFi</p>
  <svg class="abs" style="left:1000px;top:2354px" width="20" height="14" viewBox="0 0 20 14"><path d="M2 7l2-5h12l2 5v5H2z" fill="#e5535c"/><circle cx="5.5" cy="10" r="1.5" fill="#2a2a2a"/><circle cx="14.5" cy="10" r="1.5" fill="#2a2a2a"/></svg>
  <p class="abs f-text" style="left:1028px;top:2354px;font-weight:400">Free parking</p>

  <div class="abs copy">2015 © Copyright. All rights reserved</div>
</footer>

</body>
</html>
```